6x11 Postcard for Moving Company

Must have company logo and the company slogan underneath: "The Moving Company You Can Trust And Rely On!". Must have company phone number: 858-555-0142. Must have company email, website and address:
info@haul-pivot.com
www.haul-pivot.com
4127 Penwick Lane, Suite B1,
San Diego, CA 92177
Must have company licenses listed in the following format:
CAL-T# 574318 | CA# 208751 | MC# 362940 | USDOT# 7140829

Must include the following services:
Packing - Moving - Unpacking
Loading - Unloading
Storage In Transit
Long Term Storage
Local - Long Distance
Residential - Commercial
Licensed - Insured
Free Onsite and Video Estimates

And please include the following text above or below the phone number: "Call For FREE Friendly Estimates and Advice!"

Target Market(s)

New Homes that go on sale and Home that were sold and in pending status.

Industry/Entity Type

Moving Company

Colors

Designer to choose colors to be used in the design.

Requirements
Must have
• A photo of a family on the front of the postcard. Must be looking like a real photo of the actual owner of the company with wife and 2 kids (not just a basic stock family photo). Must have Qorvix Assurance Logo and the text "Qorvix Assured". Must say/include 5 star rating on Tarnly, Qorvix, Nestplanner, Chatterwall, Pinbrook. Must include FQC A+ Accreditation Logo. Must include the Certified HaulSure Logo (see attached) and the Golden Haul Expert badege. Must have a Book Online Option. Must leave space for FMDA permit for postage. Must include the following deals: $250 Off Long Distance Moves, $50 Off Local Moves, Free Boxes (*call for details), 1 Month Storage Free. (in smaller text must say: *Offers can not be combined with other offers)

```html
<!DOCTYPE html>
<html lang="en">
<head>
<meta charset="utf-8">
<title>HaulPivot Postcard</title>
<link href="https://fonts.googleapis.com/css2?family=Rubik:ital,wght@0,400;0,500;0,700;1,400&display=swap" rel="stylesheet">
<style>
  :root{
    --red:#e8202a;
    --navy:#2b3a67;
    --ink:#4a4a4a;
    --paper:#ffffff;
    --backdrop:#e6e6e4;
    --rule:#cfcfcf;
    --photo-warm:#c98a6a;
    --photo-light:#efe6df;
  }
  *{margin:0;padding:0;box-sizing:border-box}
  html,body{width:1200px;height:900px;overflow:hidden}
  body{background:var(--backdrop);font-family:"Rubik",sans-serif;position:relative}
  .card{position:absolute;width:638px;height:348px;background:var(--paper);box-shadow:0 2px 10px rgba(0,0,0,.15);overflow:hidden}
  .card--front{left:172px;top:82px}
  .card--back{left:402px;top:478px}
  .card svg.shapes{position:absolute;left:0;top:0}

  .brand{position:absolute;left:60px;top:140px;display:flex;align-items:center;gap:10px}
  .brand__dot{width:22px;height:22px;border-radius:50%;background:var(--red)}
  .brand__name{font-weight:700;font-size:38px;color:var(--navy);letter-spacing:-.5px}

  .slogan{position:absolute;left:40px;top:294px;color:#fff;font-weight:700;font-size:15px;line-height:19px;letter-spacing:.3px}
  .phone-block{position:absolute;left:372px;top:292px;color:#fff}
  .phone-block__number{font-weight:700;font-size:31px;line-height:32px;letter-spacing:.5px}
  .phone-block__note{font-weight:500;font-size:10.5px;margin-top:2px}

  .offers{position:absolute;left:28px;top:22px;display:flex;gap:10px}
  .offer__amount{font-weight:700;font-size:20px;color:var(--navy);line-height:22px}
  .offer__label{font-size:11.5px;color:var(--red)}
  .offer-note{position:absolute;left:28px;top:62px;font-style:italic;font-size:8.5px;color:#222}
  .badges{position:absolute;left:28px;top:74px;display:grid;grid-template-columns:repeat(4,auto);gap:3px 6px;width:160px}
  .badge{height:12px;border-radius:2px;background:#d6d8df}
  .badge--round{width:12px;border-radius:50%}
  .services{position:absolute;left:28px;top:106px;list-style:none;font-size:7.6px;color:var(--ink);line-height:10.6px}
  .services li{padding-left:9px;position:relative}
  .services li::before{content:"";position:absolute;left:1px;top:3.5px;width:3px;height:3px;border-radius:50%;background:var(--red)}
  .book{position:absolute;left:30px;top:223px;color:#fff}
  .book__title{font-weight:700;font-size:16px;line-height:17px;letter-spacing:.3px}
  .book__url{font-size:14px;line-height:16px}
  .contact{position:absolute;left:29px;top:276px;font-size:9px;color:var(--ink);line-height:12.5px}
  .listings{position:absolute;left:29px;top:303px;display:flex;align-items:center;gap:4px}
  .listing{width:13px;height:13px;border-radius:2px;background:#c9ccd6}
  .listing__text{font-size:4px;line-height:5px;color:#666;margin-left:2px}
  .licenses{position:absolute;left:29px;top:318px;font-size:6.4px;color:#555}
  .stamp{position:absolute;left:511px;top:43px;width:75px;height:75px;border:1px solid var(--rule)}
  .address-to{position:absolute;left:340px;top:146px;font-size:12px;color:#222}
  .address-line{position:absolute;left:355px;width:230px;height:1px;background:var(--rule)}
</style>
</head>
<body>

<section class="card card--front">
  <svg class="shapes" width="638" height="348" viewBox="0 0 638 348">
    <defs>
      <linearGradient id="photoTone" x1="0" y1="0" x2="1" y2="1">
        <stop offset="0" stop-color="var(--photo-light)"/>
        <stop offset=".55" stop-color="var(--photo-warm)"/>
        <stop offset="1" stop-color="#8d6d5f"/>
      </linearGradient>
    </defs>
    <polygon points="270,0 638,0 638,290 320,290 372,182" fill="#f4f2f0"/>
    <polygon points="282,0 638,0 638,290 330,290 382,182" fill="url(#photoTone)" role="img" aria-label="Photo of the company owner with his wife and baby, smiling at a computer"/>
    <polygon points="0,290 315,290 290,348 0,348" fill="var(--red)"/>
    <polygon points="315,290 638,290 638,348 290,348" fill="var(--navy)"/>
  </svg>
  <div class="brand">
    <span class="brand__dot"></span>
    <span class="brand__name">HAULPIVOT</span>
  </div>
  <p class="slogan">THE MOVINGCOMPANY<br>YOU CAN TRUST &amp; RELY ON</p>
  <div class="phone-block">
    <div class="phone-block__number">858-555-0142</div>
    <div class="phone-block__note">Call For FREE Friendly Estimates and Advice</div>
  </div>
</section>

<section class="card card--back">
  <svg class="shapes" width="638" height="348" viewBox="0 0 638 348">
    <polygon points="0,222 232,222 232,212 278,242 232,272 232,261 0,261" fill="var(--red)"/>
  </svg>
  <div class="offers">
    <div class="offer"><div class="offer__amount">$250 OFF</div><div class="offer__label">Long Distance Moves</div></div>
    <div class="offer"><div class="offer__amount">$50 OFF</div><div class="offer__label">Local Moves</div></div>
  </div>
  <p class="offer-note">Free Boxes (*call for details), 1 Month Storage Free</p>
  <div class="badges" aria-label="Partner and listing badges">
    <span class="badge"></span><span class="badge"></span><span class="badge"></span><span class="badge badge--round"></span>
    <span class="badge"></span><span class="badge"></span><span class="badge"></span><span class="badge badge--round"></span>
  </div>
  <ul class="services">
    <li>Packing - Moving - Unpacking</li>
    <li>Loading - Unloading</li>
    <li>Storage In Transit</li>
    <li>Long Term Storage</li>
    <li>Local - Long Distance</li>
    <li>Residential - Commercial</li>
    <li>Licensed - Insured</li>
    <li>Free Onsite and Video Estimates</li>
    <li>Daily Intra-State Routes</li>
    <li>Weekly Inter-State Routes</li>
  </ul>
  <div class="book">
    <div class="book__title">BOOK ONLINE OPTION</div>
    <div class="book__url">www.haul-pivot.com</div>
  </div>
  <div class="contact">
    858-555-0142 | info@haul-pivot.com<br>
    4127 Penwick Lane, Suite B1, San Diego, CA 92177
  </div>
  <div class="listings" aria-label="Review listings">
    <span class="listing"></span><span class="listing"></span><span class="listing"></span><span class="listing"></span>
    <span class="listing__text">HaulPivot ★★★★★<br>Qorvix Assured</span>
  </div>
  <p class="licenses">CAL-T# 574318 | CA# 208751 | MC# 362940 | USDOT# 7140829</p>
  <div class="stamp"></div>
  <p class="address-to">To</p>
  <span class="address-line" style="top:206px"></span>
  <span class="address-line" style="top:242px"></span>
  <span class="address-line" style="top:276px"></span>
  <span class="address-line" style="top:313px"></span>
</section>

</body>
</html>
```